Business Card for Managing Partner Investment Fund

To create a business card template for an investment fund manager. Business card should be more professional in nature, not too colorful, more upscale, and created using the attached logos and fund name files. I would prefer a black or gray color scheme, but am open to the use of color as well. I would prefer a double sided business card, but open to single sided business card designs as well. The business card should include: name, title, and contact information, as well as logo and company name. I would prefer a more stream-lined, simple business card design.
Updates
Address: 4190 NE 38th Ter. Ocala, FL 34470
Email: talvin47@quorimail.net
Phone: 561-347-9162
Title: managing partner
Name: Dorian Velsky
Fund Name: Ambergate Capital
Logos can be found in files attached to the brief
Target Market(s)
potential investors, other fund managers
Industry/Entity Type
Finance
Contact Information for Business Card
Name on card: Dorian Velsky
Title: Managing Partner
Colors
Designer to choose colors to be used in the design.
Requirements
Must have
- Phone number
- email address
- physical address
- title
- name
- logo
- Fund name
Nice to have
- simple layout
Should not have
- too many colors, busy fonts,

```html
<!DOCTYPE html>
<html lang="en">
<head>
<meta charset="UTF-8">
<title>Ambergate Capital – Business Card</title>
<link href="https://fonts.googleapis.com/css2?family=Open+Sans:wght@400;600&family=Saira:wght@700&display=swap" rel="stylesheet">
<style>
  :root {
    --backdrop: #2b3033;
    --card: #000000;
    --ink: #ffffff;
    --accent: #ec2024;
  }
  * { margin: 0; padding: 0; box-sizing: border-box; }
  html, body { width: 1200px; height: 1200px; overflow: hidden; }
  body {
    background: var(--backdrop);
    position: relative;
    font-family: "Open Sans", Arial, sans-serif;
    color: var(--ink);
  }
  .card {
    position: absolute;
    left: 253px;
    width: 693px;
    height: 396px;
    background: var(--card);
  }
  .card--front { top: 110px; }
  .card--back { top: 605px; }

  .holder {
    position: absolute;
    right: 30px;
    top: 20px;
    text-align: right;
  }
  .holder__name {
    font-family: "Saira", Arial, sans-serif;
    font-weight: 700;
    font-size: 31px;
    letter-spacing: 1px;
    line-height: 40px;
  }
  .holder__name .surname { color: var(--accent); }
  .holder__title {
    font-size: 17px;
    line-height: 20px;
  }

  .band { position: absolute; height: 29px; }
  .band--red { background: var(--accent); }
  .band--white { background: var(--ink); }

  .front-band-white { left: 0; top: 180px; width: 24px; }
  .front-band-red { left: 163px; top: 180px; width: 530px; }

  .wordmark {
    position: absolute;
    font-weight: 600;
    color: var(--ink);
    text-align: center;
    text-transform: uppercase;
  }
  .wordmark--small {
    left: 27px;
    top: 170px;
    width: 134px;
    font-size: 14px;
    letter-spacing: 1.5px;
    line-height: 18px;
  }
  .wordmark--large {
    left: 180px;
    top: 158px;
    width: 333px;
    font-size: 40px;
    letter-spacing: 3px;
    line-height: 48px;
  }
  .wordmark--large .wordmark__sub {
    display: block;
    font-size: 28px;
    letter-spacing: 6px;
    line-height: 38px;
  }

  .contact {
    position: absolute;
    right: 24px;
    list-style: none;
    text-align: right;
  }
  .contact__item {
    position: absolute;
    right: 0;
    display: flex;
    align-items: center;
    gap: 14px;
    white-space: nowrap;
    font-size: 15px;
  }
  .contact__icon { width: 22px; height: 22px; display: block; }
</style>
</head>
<body>

  <section class="card card--front">
    <div class="holder">
      <div class="holder__name">DORIAN <span class="surname">VELSKY</span></div>
      <div class="holder__title">MANAGING PARTNER</div>
    </div>

    <div class="band band--white front-band-white"></div>
    <div class="wordmark wordmark--small">Ambergate<br>Capital</div>
    <div class="band band--red front-band-red"></div>

    <ul class="contact" style="top:0;">
      <li class="contact__item" style="top:243px;">
        <span>4190 NE 38th Ter. Ocala, FL 34470</span>
        <svg class="contact__icon" viewBox="0 0 22 22" aria-hidden="true">
          <path d="M11 1a7 7 0 0 0-7 7c0 5 7 13 7 13s7-8 7-13a7 7 0 0 0-7-7z" fill="#fff"/>
          <circle cx="11" cy="8" r="2.6" fill="#000"/>
        </svg>
      </li>
      <li class="contact__item" style="top:283px;">
        <span>561-347-9162</span>
        <svg class="contact__icon" viewBox="0 0 22 22" aria-hidden="true">
          <rect x="5" y="1" width="12" height="20" rx="2.5" fill="#fff"/>
          <rect x="7.5" y="4" width="7" height="11" fill="#000"/>
          <circle cx="11" cy="18" r="1.2" fill="#000"/>
        </svg>
      </li>
      <li class="contact__item" style="top:320px;">
        <span>talvin47@quorimail.net</span>
        <svg class="contact__icon" viewBox="0 0 22 22" aria-hidden="true">
          <rect x="1.5" y="4.5" width="19" height="13" fill="none" stroke="#fff" stroke-width="2"/>
          <path d="M1.5 4.5 11 12l9.5-7.5M1.5 17.5l7-6M20.5 17.5l-7-6" fill="none" stroke="#fff" stroke-width="2"/>
        </svg>
      </li>
    </ul>
  </section>

  <section class="card card--back">
    <div class="band band--red" style="left:0; top:180px; width:172px;"></div>
    <div class="wordmark wordmark--large">Ambergate<span class="wordmark__sub">Capital</span></div>
    <div class="band band--white" style="left:522px; top:180px; width:171px;"></div>
  </section>

</body>
</html>
```